Coral Ridge Networks Ltd

I need a website that is an informational only. We are a construction business building telecommunications sites. Seeing how our company is Coral Ridge the color blue might want to be incorporated in the color scheme.
I can provide more picture of towers and wireless communications if needed.
current website www.coralridgenet.ca

Industry/Entity Type

Wireless Telecommunications, Construction

Coding

Coded - Design and coding required

Number of Pages Required

2 page

Font styles to use
Sans Serif

Colors

Designer to choose colors to be used in the design.

```html
<!DOCTYPE html>
<html lang="en">
<head>
<meta charset="utf-8">
<title>Coral Ridge Networks Ltd</title>
<link href="https://fonts.googleapis.com/css2?family=Jost:wght@400;500;600&display=swap" rel="stylesheet">
<style>
:root{
  --navy:#2f4a8f;
  --navy-deep:#2b3f86;
  --sky:#5fade3;
  --sky-soft:#7bbbe8;
  --page:#f1f6fc;
  --form-bg:#ebf0f7;
  --ink:#2a2f3a;
  --muted:#555d6b;
  --white:#ffffff;
  --line:#c9d3e3;
}
*{box-sizing:border-box;margin:0;padding:0}
html,body{width:1200px;height:3717px;overflow:hidden}
body{position:relative;background:var(--page);font-family:'Jost',sans-serif;color:var(--ink)}
.abs{position:absolute}
a{color:inherit;text-decoration:none}

/* header */
.site-header{left:0;top:0;width:1200px;height:120px;background:var(--page)}
.brand{left:70px;top:38px;font-size:34px;font-weight:400;color:var(--sky);letter-spacing:.5px}
.brand-sub{left:70px;top:80px;font-size:11px;letter-spacing:12px;color:var(--navy)}
.main-nav a{position:absolute;top:53px;font-size:14px;color:var(--ink)}
.main-nav .active{color:var(--navy)}
.nav-underline{left:440px;top:80px;width:40px;height:2px;background:var(--navy)}
.quote-btn{left:965px;top:39px;width:158px;height:39px;border-radius:20px;background:linear-gradient(90deg,var(--navy) 60%,var(--sky));color:#fff;font-size:14px;padding:9px 0 0 18px}

/* hero */
.hero{left:0;top:120px;width:1200px;height:675px;background:linear-gradient(160deg,#2d4f9a 0%,#3a66ad 50%,#244487 100%)}
.hero-title{left:75px;top:370px;font-size:33px;line-height:43px;color:#fff;font-weight:400}
.hero-text{left:75px;top:462px;font-size:13px;line-height:18px;color:#fff;width:320px}
.hero-btn{left:70px;top:519px;width:155px;height:39px;border-radius:20px;background:var(--sky);color:#fff;font-size:14px;text-align:center;line-height:39px}
.hero-dots{left:1130px;top:420px}
.scroll-cue{left:570px;top:765px;width:60px;height:60px;border-radius:50%;background:var(--page)}

/* intro */
.section-title{width:1200px;left:0;text-align:center;font-size:32px;line-height:42px;font-weight:400;color:var(--ink)}
.photo{border-radius:28px}
.intro-text{left:622px;top:1002px;width:470px;font-size:13px;line-height:18px;color:var(--muted)}
.check-list{left:620px;top:1125px;width:470px;list-style:none;font-size:13px;line-height:18px;color:var(--muted)}
.check-list li{position:relative;padding-left:20px;margin-bottom:18px}
.check-list svg{position:absolute;left:0;top:3px}

/* services */
.services{left:0;top:1520px;width:1200px;height:720px;background:linear-gradient(90deg,#66b3e6 0%,#4f86c9 55%,#334d92 100%)}
.services-title{color:#fff;top:1586px}
.service-card{top:1667px;width:332px;height:443px;background:#f4f8fd;border-radius:10px;overflow:hidden}
.service-photo{left:0;top:0;width:100%;height:238px}
.service-icon{left:134px;top:206px;width:64px;height:64px;border-radius:50%;background:#fff}
.service-name{left:0;top:272px;width:100%;text-align:center;font-size:17px;color:var(--ink)}
.service-rule{left:146px;top:298px;width:40px;height:2px;background:var(--navy)}
.service-text{left:26px;top:314px;width:280px;text-align:center;font-size:12.5px;line-height:18px;color:var(--muted)}

/* about */
.about-title{left:114px;top:2382px;font-size:34px;font-weight:400}
.about-rule{left:114px;top:2446px;width:39px;height:2px;background:var(--navy)}
.about-text{left:113px;top:2468px;width:470px;font-size:13px;line-height:18px;color:var(--muted)}
.about-text p{margin-bottom:18px}
.about-call{font-size:17px;color:var(--ink)}
.about-call b{font-weight:500;color:var(--navy)}

/* contact */
.quick-contact{left:0;top:2841px;width:1200px;height:418px;background:var(--form-bg)}
.qc-title{top:2905px;font-size:29px;font-weight:600;color:var(--navy-deep)}
.field{border:1px solid var(--line);border-radius:19px;background:#f7f9fc;font-size:12px;color:var(--muted);padding:10px 18px;width:280px;height:37px}
.field-msg{left:607px;top:2974px;width:280px;height:141px;border-radius:12px}
.send-btn{left:528px;top:3151px;width:141px;height:39px;border-radius:20px;background:var(--sky);color:#fff;text-align:center;line-height:39px;font-size:13px}

/* footer */
.site-footer{left:0;top:3259px;width:1200px;height:394px;background:linear-gradient(100deg,#2f4a8f 0%,#4474b8 55%,#66b2e5 100%)}
.footer-brand{left:115px;top:3390px;font-size:46px;color:#fff;font-weight:400}
.social{top:3507px;width:34px;height:34px;border-radius:50%;background:#fff}
.social.first{background:var(--sky)}
.footer-head{top:3368px;font-size:16px;font-weight:500;color:#fff;letter-spacing:.3px}
.footer-rule{top:3394px;width:56px;height:2px;background:#fff}
.footer-links{left:427px;top:3422px;list-style:none;color:#fff;font-size:13px}
.footer-links li{height:27px}
.footer-contact{left:603px;color:#fff;font-size:13px;line-height:21px}
.footer-contact svg{position:absolute;left:0;top:4px}
.footer-contact span{display:block;padding-left:22px}
.map{left:854px;top:3373px;width:271px;height:186px;border-radius:10px;background:linear-gradient(135deg,#e9ecf0,#d9dee5)}
.copyright{left:0;top:3653px;width:1200px;height:64px;background:#fff;text-align:center;line-height:64px;font-size:13px;color:var(--ink)}
.copyright b{color:var(--navy);font-weight:600}
</style>
</head>
<body>

<header class="site-header abs">
  <div class="brand abs">Coral Ridge</div>
  <nav class="main-nav">
    <a class="active" style="left:440px">Home</a>
    <a style="left:525px">About us</a>
    <a style="left:627px">Our Services</a>
    <a style="left:750px">Contact us</a>
  </nav>
  <div class="nav-underline abs"></div>
  <a class="quote-btn abs">Get A Quote
    <svg style="position:absolute;right:12px;top:15px" width="40" height="10" viewBox="0 0 40 10"><path d="M0 5h37M32 1l5 4-5 4" stroke="#fff" stroke-width="1.5" fill="none"/></svg>
  </a>
</header>

<section class="hero abs" role="img" aria-label="Telecom tower with a microwave dish against a deep blue sky"></section>
<h1 class="hero-title abs">Coral Ridge<br>Networks Ltd</h1>
<p class="hero-text abs">we are dedicated to providing our customers with friendly professional service...</p>
<a class="hero-btn abs">Read More</a>
<svg class="hero-dots abs" width="30" height="50" viewBox="0 0 30 50">
  <circle cx="10" cy="6" r="2.5" fill="#fff"/>
  <path d="M18 10a6 6 0 0 1 0 10M22 7a10 10 0 0 1 0 16M26 4a14 14 0 0 1 0 22" stroke="#fff" stroke-width="1.8" fill="none"/>
  <circle cx="10" cy="35" r="2.5" fill="#cdd8ea"/><circle cx="10" cy="46" r="2.5" fill="#cdd8ea"/>
</svg>
<div class="scroll-cue abs">
  <svg style="position:absolute;left:22px;top:13px" width="16" height="16" viewBox="0 0 16 16"><path d="M2 2l6 6 6-6M2 8l6 6 6-6" stroke="#5fade3" stroke-width="2" fill="none"/></svg>
</div>

<h2 class="section-title abs" style="top:876px">Coral Ridge<br>Networks Ltd</h2>
<div class="photo abs" style="left:112px;top:1002px;width:458px;height:378px;background:linear-gradient(180deg,#4e86cf 0%,#a9c3dc 45%,#c9ccce 70%,#8e9296 100%)" role="img" aria-label="Rooftop antenna installation with mountains in the distance"></div>
<p class="intro-text abs">Safety is number one. Coral Ridge Ltd is committed to a strong safety policy, protecting its staff and the general public from accidents and harm. All Coral Ridge Employees are certified “Tower Competent Climber and Rescue”.<br>In addition to tower safety and fall protection Coral Ridge’s safety training and practices include but are not limited to the following:</p>
<ul class="check-list abs">
  <li><svg width="13" height="13" viewBox="0 0 13 13"><circle cx="6.5" cy="6.5" r="5.5" stroke="#5fade3" fill="none"/><path d="M3.8 6.5l2 2 3.5-4" stroke="#5fade3" fill="none"/></svg>COR Certified</li>
  <li><svg width="13" height="13" viewBox="0 0 13 13"><circle cx="6.5" cy="6.5" r="5.5" stroke="#5fade3" fill="none"/><path d="M3.8 6.5l2 2 3.5-4" stroke="#5fade3" fill="none"/></svg>BC Level 1 first aid</li>
  <li><svg width="13" height="13" viewBox="0 0 13 13"><circle cx="6.5" cy="6.5" r="5.5" stroke="#5fade3" fill="none"/><path d="M3.8 6.5l2 2 3.5-4" stroke="#5fade3" fill="none"/></svg>Transportation Endorsement first aid</li>
  <li><svg width="13" height="13" viewBox="0 0 13 13"><circle cx="6.5" cy="6.5" r="5.5" stroke="#5fade3" fill="none"/><path d="M3.8 6.5l2 2 3.5-4" stroke="#5fade3" fill="none"/></svg>Sprat Level 1</li>
  <li><svg width="13" height="13" viewBox="0 0 13 13"><circle cx="6.5" cy="6.5" r="5.5" stroke="#5fade3" fill="none"/><path d="M3.8 6.5l2 2 3.5-4" stroke="#5fade3" fill="none"/></svg>On site tailboard meeting with daily checklist sign off and picture documentation</li>
  <li><svg width="13" height="13" viewBox="0 0 13 13"><circle cx="6.5" cy="6.5" r="5.5" stroke="#5fade3" fill="none"/><path d="M3.8 6.5l2 2 3.5-4" stroke="#5fade3" fill="none"/></svg>Monthly in office safety meetings</li>
  <li><svg width="13" height="13" viewBox="0 0 13 13"><circle cx="6.5" cy="6.5" r="5.5" stroke="#5fade3" fill="none"/><path d="M3.8 6.5l2 2 3.5-4" stroke="#5fade3" fill="none"/></svg>Job site specific hazard assessment and reporting</li>
</ul>

<section class="services abs"></section>
<h2 class="section-title services-title abs">Our Service</h2>

<article class="service-card abs" style="left:75px">
  <div class="service-photo abs" style="background:linear-gradient(180deg,#3f7fcf 0%,#9fbbd6 50%,#8a7a6a 75%,#6c6f72 100%)" role="img" aria-label="Rooftop antennas overlooking a city and mountains"></div>
  <div class="service-icon abs"><svg style="margin:16px" width="32" height="32" viewBox="0 0 32 32"><rect x="6" y="10" width="14" height="20" stroke="#2a2f3a" fill="none" stroke-width="1.5"/><path d="M22 30V14l4-8 4 8v16" stroke="#2a2f3a" fill="none" stroke-width="1.5"/></svg></div>
  <h3 class="service-name abs">Rooftop Sites</h3><div class="service-rule abs"></div>
  <p class="service-text abs">Structural upgrades or simple ballast mounts. Shelter on the ground, leasehold build outs or cabinets on the roof. Coral Ridge can install what you need where you need it.</p>
</article>
<article class="service-card abs" style="left:434px">
  <div class="service-photo abs" style="background:linear-gradient(180deg,#3e4f66 0%,#6f8198 60%,#8d9aa8 100%)" role="img" aria-label="Lattice tower with dish antennas against a grey sky"></div>
  <div class="service-icon abs"><svg style="margin:16px" width="32" height="32" viewBox="0 0 32 32"><path d="M16 8L9 30M16 8l7 22M11 23h10" stroke="#2a2f3a" fill="none" stroke-width="1.5"/><path d="M10 4a8 8 0 0 0 0 8M22 4a8 8 0 0 1 0 8" stroke="#2a2f3a" fill="none" stroke-width="1.5"/></svg></div>
  <h3 class="service-name abs">Towers and Monopoles</h3><div class="service-rule abs"></div>
  <p class="service-text abs">Coral Ridge can engineer, supply and install all your tower needs. New structures or existing, call us for pricing we would be happy to help out.</p>
</article>
<article class="service-card abs" style="left:793px">
  <div class="service-photo abs" style="background:linear-gradient(180deg,#8ea3ad 0%,#4f6b45 45%,#6c6a55 75%,#77706a 100%)" role="img" aria-label="Forest construction site with concrete foundations"></div>
  <div class="service-icon abs"><svg style="margin:16px" width="32" height="32" viewBox="0 0 32 32"><path d="M16 10L11 30M16 10l5 20M12.5 24h7" stroke="#2a2f3a" fill="none" stroke-width="1.5"/><path d="M9 5a9 9 0 0 0 0 9M23 5a9 9 0 0 1 0 9" stroke="#2a2f3a" fill="none" stroke-width="1.5"/></svg></div>
  <h3 class="service-name abs">In Building</h3><div class="service-rule abs"></div>
  <p class="service-text abs">Small office or large Hotel. Coral Ridge has installed services into all size buildings. Fiber, cat6, or coax, we have the abilities to install, test, and get the job done.</p>
</article>

<h2 class="about-title abs">About us</h2>
<div class="about-rule abs"></div>
<div class="about-text abs">
  <p>At Coral Ridge Ltd, we are dedicated to providing our customers with friendly professional service. We value your business. We have made it our mission to provide reliable products and services in our customer-driven approach.</p>
  <p>Our courteous, professional team is able to support a range of services to meet your requirements.</p>
  <p style="margin-bottom:8px">To learn more about Coral Ridge Ltd, and the products and services we can offer,</p>
  <p class="about-call">Please Call us at <b>1-604-555-0192</b>.</p>
</div>
<div class="photo abs" style="left:629px;top:2340px;width:458px;height:377px;background:linear-gradient(180deg,#8fb3d8 0%,#c5d8ea 55%,#eef2f6 100%)" role="img" aria-label="Radome antenna on a snowy mountain summit"></div>

<section class="quick-contact abs"></section>
<h2 class="section-title qc-title abs">QUICK CONTACT</h2>
<div class="field abs" style="left:313px;top:2974px">Name*</div>
<div class="field abs" style="left:313px;top:3026px">Phone*</div>
<div class="field abs" style="left:313px;top:3077px">Email*</div>
<div class="field field-msg abs">Message</div>
<a class="send-btn abs">Send</a>

<footer class="site-footer abs"></footer>
<div class="footer-brand abs">Coral Ridge</div>
<div class="social first abs" style="left:114px"></div>
<div class="social abs" style="left:162px"></div>
<div class="social abs" style="left:211px"></div>
<div class="social abs" style="left:257px"></div>

<h4 class="footer-head abs" style="left:427px">QUICK LINKS</h4>
<div class="footer-rule abs" style="left:427px"></div>
<ul class="footer-links abs">
  <li>&gt;&nbsp; Home</li><li>&gt;&nbsp; About us</li><li>&gt;&nbsp; Our Services</li><li>&gt;&nbsp; Contact us</li>
</ul>

<h4 class="footer-head abs" style="left:603px">CONTACT DETAIL</h4>
<div class="footer-rule abs" style="left:603px"></div>
<div class="footer-contact abs" style="top:3425px"><svg width="11" height="11" viewBox="0 0 11 11"><path d="M2 1l2 0 1 2.5-1.3 1a6 6 0 0 0 2.8 2.8l1-1.3L10 7v2a1 1 0 0 1-1 1A8 8 0 0 1 1 2a1 1 0 0 1 1-1z" fill="#fff"/></svg><span>1-604-555-0192</span></div>
<div class="footer-contact abs" style="top:3470px"><svg width="11" height="9" viewBox="0 0 11 9"><rect x=".5" y=".5" width="10" height="8" fill="none" stroke="#fff"/><path d="M.5 .5l5 4 5-4" stroke="#fff" fill="none"/></svg><span>info@coralridgenet.ca</span></div>
<div class="footer-contact abs" style="top:3516px"><svg width="10" height="13" viewBox="0 0 10 13"><path d="M5 12S1 7.5 1 5a4 4 0 0 1 8 0c0 2.5-4 7-4 7z" fill="none" stroke="#fff" stroke-width="1.3"/><circle cx="5" cy="5" r="1.4" fill="#fff"/></svg><span>4120 Harbour Lane Westvale, BC<br>V0X 1A0</span></div>

<div class="map abs" role="img" aria-label="Street map showing the office location"></div>

<div class="copyright abs">Copyright © 2022 <b>CORAL RIDGE</b>, All Rights Reserved.</div>

</body>
</html>
```